Wordpress template re-design of current website

We need a WordPress template design and new look for our existing website. Our existing site it located at www.velmoro.com.au We are a tech company and want a fresh, clean modern website that matches our brand, services and logo colors. Our main Services are hospitality solutions, Velmoro TV solution and managed networks, more information on these can come from our existing website.

Target Market(s)

We are a tech company so must have a modern feel for new technology

Industry/Entity Type

It Company

Number of Pages Required

5+ page

Font styles to use
Sans Serif

Requirements
Must have
• Be based on a wordpress templete design and match the services that we have in our existing website, in the testimonials want a place for video testimonials as well as text. Nice clean icons used for graphics to represent services.
Nice to have
• nice visual representation of our services in the way of clean icons etc
Should not have
• Clutter

```html
<!DOCTYPE html>
<html lang="en">
<head>
<meta charset="utf-8">
<title>Velmoro Wireless Internet</title>
<link href="https://fonts.googleapis.com/css2?family=Open+Sans:wght@400;600;700;800&display=swap" rel="stylesheet">
<style>
:root{
  --navy:#0d3f7a;
  --navy-dark:#0a2f5c;
  --ink:#222;
  --muted:#555;
  --sky-top:#6a8fd0;
  --sky-bottom:#c9d8ee;
  --band:#5a86b6;
  --footer:#5b86b7;
  --line:#b9c6d8;
  --white:#fff;
}
*{margin:0;padding:0;box-sizing:border-box}
html,body{width:1200px;height:4036px;overflow:hidden}
body{font-family:"Open Sans",Arial,sans-serif;color:var(--ink);background:var(--white);position:relative}
.abs{position:absolute}

/* header */
.site-header{position:absolute;top:0;left:0;width:1200px;height:82px;background:var(--white)}
.brand{position:absolute;left:100px;top:20px;display:flex;align-items:center;gap:10px}
.brand-name{font-weight:800;font-style:normal;font-size:30px;color:var(--navy);line-height:1}
.brand-dot{width:18px;height:18px;border-radius:50%;background:var(--navy)}
.main-nav{position:absolute;right:105px;top:30px;display:flex;gap:26px;align-items:center}
.main-nav a{font-size:18px;font-weight:700;letter-spacing:1.5px;color:var(--navy);text-decoration:none}
.main-nav a.active{background:var(--navy);color:var(--white);padding:3px 14px;border-radius:14px}

/* hero */
.hero{position:absolute;top:82px;left:0;width:1200px;height:773px;background:linear-gradient(180deg,var(--sky-top),#8eaadf 55%,var(--sky-bottom))}
.hero-text{position:absolute;top:330px;left:0;width:1200px;text-align:center;color:var(--white)}
.hero-kicker{font-size:30px;letter-spacing:14px;font-weight:400}
.hero-title{font-size:44px;font-weight:700;letter-spacing:3px;margin-top:8px}
.hero-sub{font-size:35px;font-weight:600;letter-spacing:2px;color:#0c1830;margin-top:6px}
.hero-btn{display:inline-block;margin-top:40px;background:var(--navy);color:var(--white);font-size:17px;font-weight:700;letter-spacing:2px;padding:14px 50px;border-radius:26px}
.hero-dots{position:absolute;bottom:10px;left:0;width:1200px;display:flex;justify-content:center;gap:8px}
.hero-dots span{width:20px;height:20px;border-radius:50%;border:3px solid var(--white);background:transparent}
.hero-dots span.on{background:var(--navy)}

/* section heading */
.sec-title{position:absolute;left:0;width:1200px;text-align:center;font-size:44px;font-weight:800;letter-spacing:4px;color:var(--navy)}
.sec-title::after{content:"";display:block;width:280px;margin:14px auto 0;border-bottom:2px dotted var(--line)}
.sec-intro{position:absolute;left:115px;width:970px;text-align:center;font-size:17px;line-height:1.35;color:var(--ink)}

/* services tabs */
.tab-list{position:absolute;left:110px;top:1100px;width:430px;list-style:none}
.tab-list li{height:48px;display:flex;justify-content:space-between;align-items:center;padding:0 6px;border-bottom:2px dotted var(--line);font-size:22px;font-weight:700;letter-spacing:1.5px;color:var(--navy)}
.tab-list li .num{font-weight:400;color:#aab4c4;font-size:20px}
.tab-list li.active{background:var(--navy);color:var(--white);clip-path:polygon(0 0,93% 0,100% 50%,93% 100%,0 100%);width:430px;border-bottom:none}
.tab-panel{position:absolute;left:578px;top:1110px;width:520px}
.tab-panel h3{font-size:23px;font-weight:700;letter-spacing:1.5px;color:var(--ink)}
.tab-panel p{font-size:17px;line-height:1.3;margin-top:22px;color:var(--ink)}
.network-art{position:absolute;left:560px;top:1270px;width:545px;height:245px;border-radius:6px;background:linear-gradient(135deg,#e6eef7,#bdd0e6 60%,#8fb093)}

/* features */
.feature{position:absolute;left:113px;width:780px;height:110px}
.feature-icon{position:absolute;left:0;top:0;width:94px;height:94px;border-radius:50%;background:var(--navy);display:flex;align-items:center;justify-content:center}
.feature h3{position:absolute;left:115px;top:0;font-size:30px;font-weight:700;letter-spacing:1px;color:var(--ink)}
.feature p{position:absolute;left:115px;top:48px;width:660px;font-size:17px;line-height:1.3;color:var(--muted)}
.monitor-art{position:absolute;left:905px;top:1695px;width:295px;height:480px;background:linear-gradient(160deg,#d7dbe1,#8f6fb0 35%,#d98bb0 60%,#e9ecef 80%)}

/* quote band */
.quote-band{position:absolute;top:2212px;left:0;width:1200px;height:490px;background:linear-gradient(120deg,#6d8fb3,#a9b9c4 45%,#8eb0c9)}
.quote-mark{position:absolute;top:130px;left:0;width:1200px;text-align:center;font-size:160px;font-weight:800;color:var(--navy);line-height:1}
.quote-text{position:absolute;top:218px;left:140px;width:920px;text-align:center;font-size:32px;font-weight:700;letter-spacing:2px;line-height:1.15;color:var(--white)}

/* help */
.help{position:absolute;top:2702px;left:0;width:1200px;height:488px;background:var(--band);color:var(--white)}
.help .sec-title{color:var(--white);top:28px}
.help .sec-title::after{border-color:#a9c0dc}
.help .sec-intro{color:#0d1d33;top:112px}
.laptop-art{position:absolute;left:98px;top:175px;width:450px;height:285px;background:linear-gradient(180deg,#2b2b2b 0%,#2b2b2b 86%,#c9ccd1 86%);border-radius:10px 10px 4px 4px}
.laptop-art::before{content:"";position:absolute;left:22px;top:20px;right:22px;height:205px;background:#f4f6f9}
.solution{position:absolute;left:618px;top:188px;width:460px}
.solution h3{font-size:27px;font-weight:700;letter-spacing:1.5px}
.solution p{font-size:17px;line-height:1.3;margin-top:10px;color:#0d1d33}
.solution ul{margin-top:8px;list-style:none}
.solution li{font-size:17px;line-height:1.45;color:#0d1d33;padding-left:18px;position:relative}
.solution li::before{content:"";position:absolute;left:2px;top:9px;width:7px;height:7px;border-radius:50%;background:var(--white)}

/* clients */
.clients{position:absolute;top:3190px;left:0;width:1200px;height:490px;background:linear-gradient(180deg,#eef0f3,#d6dbe2)}
.clients .sec-title{top:16px;color:var(--navy)}
.client{position:absolute;width:205px;height:76px;border:3px solid #222;background:var(--white);display:flex;align-items:center;justify-content:center;font-size:21px;font-weight:700;color:var(--ink)}

/* footer */
.site-footer{position:absolute;top:3680px;left:0;width:1200px;height:356px;background:var(--footer);color:var(--white)}
.foot-col{position:absolute;top:30px}
.foot-col h4{font-size:27px;font-weight:700;letter-spacing:3px}
.foot-col h4::after{content:"";display:block;width:160px;margin-top:6px;border-bottom:2px dotted #a9c0dc}
.foot-about p{font-size:16px;line-height:1.25;margin-top:20px;width:270px;color:#0d1d33}
.foot-more{margin-top:18px;font-size:14px;font-weight:700;letter-spacing:1px;color:#0d1d33}
.divider{position:absolute;top:30px;height:280px;border-left:3px dotted #0d1d33}
.foot-links{list-style:none;top:72px}
.foot-links li{font-size:27px;font-weight:700;letter-spacing:2px;line-height:1.7;color:var(--white)}
.foot-links li span{margin-right:12px}
.contact-row{display:flex;gap:14px;align-items:flex-start;font-size:17px;line-height:1.25;color:#0d1d33;margin-top:10px}
.contact-row:first-of-type{margin-top:26px}
.social{display:flex;gap:16px;margin-top:26px}
.social span{width:56px;height:56px;border-radius:50%;background:#0b0b0b}
</style>
</head>
<body>

<header class="site-header">
  <div class="brand"><span class="brand-name">Velmoro</span><span class="brand-dot"></span></div>
  <nav class="main-nav">
    <a class="active">HOME</a><a>SERVICES ▾</a><a>ABOUT</a><a>OURWORK</a><a>CONTACT</a><a>PORTAL</a>
  </nav>
</header>

<section class="hero" role="img" aria-label="Mobile communications tower against a blue cloudy sky">
  <div class="hero-text">
    <div class="hero-kicker">WELCOME TO</div>
    <div class="hero-title">VELMORO WIRELESS INTERNET</div>
    <div class="hero-sub">Full Mobile 3G &amp; 4G Solutions</div>
    <div class="hero-btn">READ MORE</div>
  </div>
  <div class="hero-dots"><span></span><span class="on"></span><span></span></div>
</section>

<section class="services">
  <h2 class="sec-title" style="top:900px">OUR SERVICES</h2>
  <p class="sec-intro" style="top:985px">Our high quality Wi Fi networks offer a robust 24/7 connectivity, enhancing our client's hospitality services. Whether travelling for business or pleasure, guests like to stay connected with their families, friends, and more importantly, with their work.</p>
  <ul class="tab-list">
    <li class="active">HOSPITALITY SOLUTIONS</li>
    <li>VELMORO TV SOLUTIONS <span class="num">02</span></li>
    <li>MANAGED NETWORKS <span class="num">03</span></li>
    <li>MINING AND REMOTE <span class="num">04</span></li>
    <li>MOBILE SOUTIONS <span class="num">05</span></li>
  </ul>
  <div class="tab-panel">
    <h3>HOSPITALITY SOLUTIONS</h3>
    <p>Our high quality Wi Fi networks offer a robust 24/7 connectivity, enhancing our client's hospitality services. Whether travelling for business or pleasure, guests like to stay connected with their families, friends, and more importantly, with their work.</p>
  </div>
  <div class="network-art" role="img" aria-label="Illustration of a hotel wireless network connecting rooms and devices"></div>
</section>

<section class="features">
  <h2 class="sec-title" style="top:1585px">VELMORO WIRELESS</h2>
  <div class="feature" style="top:1680px">
    <div class="feature-icon"><svg width="50" height="44" viewBox="0 0 50 44" fill="none" stroke="#fff" stroke-width="5" stroke-linecap="round"><path d="M4 16a30 30 0 0 1 42 0"/><path d="M12 24a19 19 0 0 1 26 0"/><path d="M19 32a9 9 0 0 1 12 0"/><circle cx="25" cy="39" r="3" fill="#fff" stroke="none"/></svg></div>
    <h3>Wi-Fi Hotspots</h3>
    <p>Leading supplier of public access and internet billing systems.</p>
  </div>
  <div class="feature" style="top:1787px">
    <div class="feature-icon"><svg width="50" height="44" viewBox="0 0 50 44" fill="none" stroke="#fff" stroke-width="4"><rect x="3" y="4" width="44" height="28" rx="2"/><path d="M17 40h16M25 32v8"/></svg></div>
    <h3>Velmoro TV</h3>
    <p>Turn you standard TV into a full guest information system and point of sale.</p>
  </div>
  <div class="feature" style="top:1900px">
    <div class="feature-icon"><svg width="40" height="44" viewBox="0 0 40 44"><text x="20" y="37" text-anchor="middle" font-family="Open Sans,Arial,sans-serif" font-weight="800" font-size="40" fill="#fff">H</text></svg></div>
    <h3>HSIA Solutions</h3>
    <p>Our guest access solutions have been built with the guest in mind and are easy to use</p>
  </div>
  <div class="feature" style="top:2017px">
    <div class="feature-icon"><svg width="48" height="44" viewBox="0 0 48 44" fill="none" stroke="#fff" stroke-width="4" stroke-linejoin="round"><path d="M6 6h36v24H20l-9 8v-8H6z"/></svg></div>
    <h3>Social Wi-Fi</h3>
    <p>Get more out of your existing Wi-Fi with our social plug-ins to gain valuble insight into users</p>
  </div>
  <div class="monitor-art" role="img" aria-label="Desktop computer monitor with keyboard and mouse"></div>
</section>

<section class="quote-band" role="img" aria-label="Background photo of a smiling woman using a phone with a coffee cup">
  <div class="quote-mark">“</div>
  <p class="quote-text">We strive to out work our competition with an effective approach and a powerful skill set, which is why were industry leading.</p>
</section>

<section class="help">
  <h2 class="sec-title">HOW CAN WE HELP</h2>
  <p class="sec-intro">Lorem Ipsum is simply dummy text of the printing and typesetting industry. Lorem Ipsum has been the industry's standard dummy text ever since the 1500s</p>
  <div class="laptop-art" role="img" aria-label="Laptop showing the Velmoro home screen"></div>
  <div class="solution">
    <h3>VELMORO SOLUTION</h3>
    <p>Lorem Ipsum is simply dummy text of the printing and typesetting industry. Lorem Ipsum has been the industry's standard dummy text ever since the 1500s</p>
    <ul>
      <li>Strong, Stable Network</li>
      <li>Easy to use</li>
      <li>Stay In Touch</li>
      <li>Full support options</li>
    </ul>
  </div>
</section>

<section class="clients" role="img" aria-label="Faint collage of professional portrait photos behind the client list">
  <h2 class="sec-title">LIST OF TRUSTED CLIENTS</h2>
  <div class="client" style="left:170px;top:155px">Harbour Stay</div>
  <div class="client" style="left:395px;top:155px">Ridgeway Tours</div>
  <div class="client" style="left:620px;top:155px">Roamly</div>
  <div class="client" style="left:845px;top:155px">Camplink</div>
  <div class="client" style="left:395px;top:270px">Stonevale</div>
  <div class="client" style="left:620px;top:270px">Larkfield</div>
</section>

<footer class="site-footer">
  <div class="foot-col foot-about" style="left:105px">
    <h4>ABOUT US</h4>
    <p>Velmoro Wireless has been a leader in wireless networks and internet billing systems for over a decade. Velmoro currently has completed over 2000 installations.</p>
    <div class="foot-more">MORE ›</div>
  </div>
  <div class="divider" style="left:395px"></div>
  <ul class="foot-col foot-links" style="left:420px">
    <li><span>›</span>CASE STUDIES</li>
    <li><span>›</span>TESTIMONIALS</li>
    <li><span>›</span>NEWS</li>
    <li><span>›</span>RESELLERS</li>
  </ul>
  <div class="divider" style="left:755px"></div>
  <div class="foot-col" style="left:787px">
    <h4>CONTACT US</h4>
    <div class="contact-row"><svg width="16" height="22" viewBox="0 0 16 22"><path d="M8 0a8 8 0 0 1 8 8c0 6-8 14-8 14S0 14 0 8a8 8 0 0 1 8-8z" fill="#0b0b0b"/><circle cx="8" cy="8" r="3" fill="#5b86b7"/></svg><span>210 Marlin Parade<br>Seaview Lakes, QLD 4299</span></div>
    <div class="contact-row"><svg width="18" height="18" viewBox="0 0 24 24"><path d="M6.6 10.8a15 15 0 0 0 6.6 6.6l2.2-2.2a1 1 0 0 1 1-.25 11 11 0 0 0 3.6.6 1 1 0 0 1 1 1V20a1 1 0 0 1-1 1A17 17 0 0 1 3 4a1 1 0 0 1 1-1h3.5a1 1 0 0 1 1 1 11 11 0 0 0 .6 3.6 1 1 0 0 1-.25 1z" fill="#0b0b0b"/></svg><span>1300 555 014</span></div>
    <div class="contact-row"><svg width="18" height="14" viewBox="0 0 18 14"><rect width="18" height="14" rx="1" fill="#0b0b0b"/><path d="M1 1l8 7 8-7" fill="none" stroke="#5b86b7" stroke-width="1.5"/></svg><span>sales@velmoro.com.au</span></div>
    <div class="social"><span></span><span></span></div>
  </div>
</footer>

</body>
</html>
```